Business Card

We would like a very clean corporate, two sided business card that conveys that we are a quality focused, reliable organisation that can make a business better. We focus on a cycle of continuous improvement for IT systems.

The brief is primarily clean and corporate, nothing overly complicated.

We sell IT services, IT support, server implementation, problem solving services to businesses in Australia.

Business

```html
<!DOCTYPE html>
<html lang="en">
<head>
<meta charset="utf-8">
<title>Steadyline Business Card Concepts</title>
<link rel="stylesheet" href="https://fonts.googleapis.com/css2?family=Open+Sans:wght@400;600&display=swap">
<style>
:root{
  --pink:#e5144f;
  --pink-mid:#ee3f69;
  --pink-soft:#f7849d;
  --ink:#1d1d1f;
  --white:#ffffff;
  --grey-1:#f4f4f4;
  --grey-2:#dcdcdc;
  --page:#ffffff;
}
*{margin:0;padding:0;box-sizing:border-box}
html,body{width:1200px;height:1042px;overflow:hidden;background:var(--page)}
body{position:relative;font-family:"Open Sans",Arial,sans-serif;color:var(--ink)}
.card{position:absolute;overflow:hidden;background:var(--white)}
.abs{position:absolute}
.brand{position:absolute;display:flex;align-items:center;gap:10px;font-family:"Open Sans",Arial,sans-serif;font-weight:600;color:var(--ink);font-size:40px;letter-spacing:-0.5px;line-height:1}
.brand-dot{width:18px;height:18px;background:var(--pink);border-radius:50%}
.band-top{position:absolute;left:0;top:0;height:30px;width:100%;background:linear-gradient(90deg,var(--pink-mid),var(--pink-soft) 70%,#fbd0da)}
.band-pink{position:absolute;background:linear-gradient(90deg,var(--pink),var(--pink-mid) 55%,var(--pink-soft))}
.band-pink-v{position:absolute;background:linear-gradient(90deg,var(--pink-soft),var(--pink-mid) 55%,var(--pink))}
.contact{color:var(--white);font-size:12.5px;line-height:1.35}
.contact-dark{color:var(--ink)}
.row-line{position:absolute;display:flex;justify-content:space-between;font-size:12.5px}
.it-big{position:absolute;font-weight:400;line-height:0.8;letter-spacing:-4px}
.services{position:absolute;line-height:1.3;white-space:nowrap}
.grey-card{background:linear-gradient(180deg,var(--grey-1),var(--white) 45%,var(--grey-2))}
.outline{border:1px solid #9a9a9a}
</style>
</head>
<body>

<!-- Row 1 left: front with contact band -->
<section class="card" style="left:0;top:0;width:547px;height:308px">
  <div class="band-top"></div>
  <div class="brand" style="left:130px;top:78px"><span>steadyline</span><span class="brand-dot"></span></div>
  <div class="band-pink" style="left:0;top:185px;width:547px;height:123px"></div>
  <p class="abs contact" style="left:0;top:214px;width:547px;text-align:center">Steadyline Pty Ltd,Suite 210, 48 Harbour Lane,Lane Cove, NSW, 2066<br>Australia</p>
  <div class="row-line contact" style="left:20px;top:265px;width:510px"><span>PH: +61 2 5550 1820</span><span>FAX: +61 2 5550 1821</span><span>ABN: 12 345 678 901</span></div>
</section>

<!-- Row 1 right: back with services band -->
<section class="card" style="left:655px;top:0;width:545px;height:308px">
  <div class="band-top"></div>
  <div class="brand" style="left:35px;top:78px"><span>steadyline</span><span class="brand-dot"></span></div>
  <div class="band-pink" style="left:0;top:185px;width:545px;height:123px"></div>
  <div class="it-big" style="left:230px;top:174px;font-size:92px;line-height:1;letter-spacing:-3px;color:var(--white)">IT</div>
  <div class="services" style="left:316px;top:190px;font-size:23px;color:var(--white)">Consulting</div>
  <div class="services" style="left:348px;top:222px;font-size:23px;color:var(--white)">Outsourcing</div>
  <div class="services" style="left:240px;top:262px;font-size:23px;color:var(--white)">Managed Services</div>
</section>

<!-- Row 2 left: side panel contact -->
<section class="card" style="left:0;top:359px;width:547px;height:306px">
  <div class="band-pink-v" style="left:0;top:0;width:28px;height:306px"></div>
  <div class="brand" style="left:40px;top:90px;font-size:36px"><span>steadyline</span><span class="brand-dot"></span></div>
  <div class="band-pink-v" style="left:313px;top:0;width:234px;height:306px"></div>
  <p class="abs contact" style="left:335px;top:72px;font-size:13px;line-height:1.3">Steadyline Pty Ltd,<br>Suite 210, 48 Harbour Lane,<br>Lane Cove, NSW, 2066<br>Australia<br>PH: +61 2 5550 1820<br>FAX: +61 2 5550 1821<br>ABN: 12 345 678 901</p>
</section>

<!-- Row 2 right: side panel services -->
<section class="card" style="left:655px;top:359px;width:545px;height:306px">
  <div class="band-pink-v" style="left:0;top:0;width:28px;height:306px"></div>
  <div class="brand" style="left:40px;top:95px;font-size:36px"><span>steadyline</span><span class="brand-dot"></span></div>
  <div class="band-pink-v" style="left:306px;top:0;width:239px;height:306px"></div>
  <div class="it-big" style="left:326px;top:28px;font-size:190px;color:var(--white)">IT</div>
  <div class="services" style="left:326px;top:188px;font-size:17px;color:var(--white);line-height:1.25">Consulting<br>Outsourcing<br>Managed Services</div>
</section>

<!-- Row 3 left: light card contact -->
<section class="card grey-card" style="left:0;top:723px;width:547px;height:312px">
  <svg class="abs" style="left:0;top:0" width="547" height="312" viewBox="0 0 547 312" aria-hidden="true">
    <polygon points="0,38 18,70 18,205 0,235" fill="var(--pink-mid)"/>
    <polygon points="547,38 529,70 529,205 547,235" fill="var(--pink-mid)"/>
  </svg>
  <div class="brand" style="left:133px;top:36px"><span>steadyline</span><span class="brand-dot"></span></div>
  <p class="abs contact-dark" style="left:0;top:226px;width:547px;text-align:center;font-size:12.5px;line-height:1.35">Steadyline Pty Ltd,Suite 210, 48 Harbour Lane,Lane Cove, NSW, 2066<br>Australia</p>
  <div class="row-line contact-dark" style="left:30px;top:285px;width:495px"><span>PH: +61 2 5550 1820</span><span>FAX: +61 2 5550 1821</span><span>ABN: 12 345 678 901</span></div>
</section>

<!-- Row 3 right: light card services -->
<section class="card grey-card outline" style="left:660px;top:725px;width:540px;height:306px">
  <svg class="abs" style="left:0;top:0" width="540" height="306" viewBox="0 0 540 306" aria-hidden="true">
    <polygon points="0,40 16,70 16,205 0,235" fill="var(--pink-mid)"/>
    <polygon points="540,40 524,70 524,205 540,235" fill="var(--pink-mid)"/>
  </svg>
  <div class="brand" style="left:50px;top:22px"><span>steadyline</span><span class="brand-dot"></span></div>
  <div class="it-big" style="left:36px;top:128px;font-size:150px;color:var(--pink)">IT</div>
  <div class="services" style="left:168px;top:130px;font-size:24px;line-height:1.65">Consulting<br>Outsourcing<br>Managed Services</div>
</section>

</body>
</html>
```